Heron Landing Post Card

I am a real estate agent with Marlowe and Partners. I would like to have two post cards designed. A Just Listed and a Just Sold post card for the bay front community of Heron Landing. Heron Landing is a residential community located on the Gulf coast of Florida. It is bordered by Osprey Sound on one side of the road and Pelican Reef Golf Course on the other side of the road. I am uploading several images that can be used on the design of the postcard as well as an example of what I would like to be included on the back. They will be oversized postcards and color on both sides.

Industry/Entity Type

Real Estate

```html
<!DOCTYPE html>
<html lang="en">
<head>
<meta charset="utf-8">
<title>Heron Landing – Just Listed Postcard</title>
<link rel="stylesheet" href="https://fonts.googleapis.com/css2?family=Merriweather:wght@300;400;700&family=Open+Sans:wght@400;600&display=swap">
<style>
  :root {
    --page-bg: #d9d6d0;
    --card-white: #f6f7f9;
    --ink-dark: #111111;
    --ink-mid: #2e2e2e;
    --glow: #8a8a8a;
    --brand-blue: #1a7bc4;
    --text-blue: #1f7cc0;
    --body-ink: #222222;
    --photo-frame: #ffffff;
    --sky: #a9bfd8;
    --foliage: #5f7a4a;
    --lawn: #6d8a3e;
    --water: #7d8fa6;
  }
  * { margin: 0; padding: 0; box-sizing: border-box; }
  html, body {
    width: 1200px; height: 791px; overflow: hidden;
    background: var(--page-bg);
  }
  .postcard {
    position: absolute; left: 21px; top: 21px;
    width: 1158px; height: 749px;
    background: linear-gradient(180deg, var(--card-white) 40%, #eceef1 100%);
    box-shadow: 0 3px 10px rgba(0,0,0,0.25);
    overflow: hidden;
  }
  .header-band { position: absolute; inset: 0; width: 1158px; height: 749px; }
  .headline {
    position: absolute; left: 51px; top: 76px;
    font-family: "Merriweather", Georgia, serif;
    font-weight: 400; font-size: 76px; letter-spacing: 1px;
    color: #ffffff;
    text-shadow: 3px 3px 0 #000, 4px 4px 6px rgba(0,0,0,0.6);
  }
  .brand {
    position: absolute; left: 735px; top: 62px;
    width: 340px; height: 120px;
    display: flex; align-items: center; gap: 16px;
  }
  .brand-square {
    width: 26px; height: 26px; flex: none;
    background: var(--brand-blue);
  }
  .brand-name {
    font-family: "Merriweather", Georgia, serif;
    font-weight: 700; font-size: 30px; line-height: 1.2;
    color: #ffffff;
  }
  .agent {
    position: absolute; left: 750px; top: 236px; width: 300px;
    text-align: center;
    font-family: "Open Sans", Arial, sans-serif;
    font-size: 24px; color: var(--body-ink);
  }
  .photo {
    position: absolute;
    border: 5px solid var(--photo-frame);
    box-shadow: 0 4px 10px rgba(0,0,0,0.35);
  }
  .photo-home {
    left: 128px; top: 359px; width: 349px; height: 201px;
    background: linear-gradient(180deg, var(--sky) 0%, #dfe3e6 35%, #cfd3d2 60%, var(--foliage) 85%);
  }
  .photo-community {
    left: 511px; top: 300px; width: 599px; height: 343px;
    background: linear-gradient(180deg, var(--sky) 0%, #dde4ee 30%, #b9c2b4 44%, var(--lawn) 58%, var(--lawn) 70%, var(--water) 85%, #8d9a7a 100%);
  }
  .community-name {
    position: absolute; left: 41px; top: 608px;
    font-family: "Merriweather", Georgia, serif;
    font-weight: 300; font-size: 44px; line-height: 58px;
    color: var(--text-blue); text-transform: uppercase;
  }
</style>
</head>
<body>
  <main class="postcard">
    <svg class="header-band" viewBox="0 0 1158 749" aria-hidden="true">
      <defs>
        <radialGradient id="band-glow" cx="0.42" cy="0.12" r="0.6">
          <stop offset="0" stop-color="var(--glow)"/>
          <stop offset="0.45" stop-color="var(--ink-mid)"/>
          <stop offset="1" stop-color="var(--ink-dark)"/>
        </radialGradient>
      </defs>
      <path d="M0 0 H1158 V150 C700 160 300 250 0 379 Z" fill="url(#band-glow)"/>
      <path d="M0 379 C300 250 700 160 1158 150" fill="none" stroke="var(--brand-blue)" stroke-width="9"/>
      <path d="M0 391 C300 262 700 172 1158 162" fill="none" stroke="#ffffff" stroke-width="5"/>
      <path d="M0 398 C300 269 700 179 1158 169" fill="none" stroke="var(--brand-blue)" stroke-width="3"/>
    </svg>

    <h1 class="headline">JUST LISTED</h1>

    <div class="brand">
      <span class="brand-square"></span>
      <span class="brand-name">Marlowe and Partners</span>
    </div>
    <p class="agent">Clara Whitfield Broker</p>

    <div class="photo photo-home" role="img" aria-label="Photo of a white two-story coastal home with a metal roof and palm trees"></div>
    <div class="photo photo-community" role="img" aria-label="Photo of waterfront homes across a pond and golf course lawn"></div>

    <h2 class="community-name">Heron Landing<br>A Bay Front Community</h2>
  </main>
</body>
</html>
```